Flyer Design Project

We are a Human Resources and payroll company with a dedicated staffing and recruiting division. We need a really professional looking and creative flyer that breifly explains our offerings. This flyer will be given to other sales people that sell complementary services to what we offer. Those salespeople will to leave this flyer with prospective clients that want services that do not offer and we do.
Updates

I just uploades our logo in EPS!  Thank you!

Target Market(s)

Employers are our target market. Mostly healthcare but not exclusively.

Industry/Entity Type

It Company

Requirements
Must have
• Photos of people in a working environment would be good. All offering in attached files must be in the flyer as well as our logo.
Nice to have
• It would be nice to convey that we care about our clients and their employees.

```html
<!DOCTYPE html>
<html lang="en">
<head>
<meta charset="utf-8">
<title>Meridian HR Employee Solutions – Service Flyer</title>
<link rel="stylesheet" href="https://fonts.googleapis.com/css2?family=Carlito:ital,wght@0,400;0,700;1,400&family=Arimo:wght@400;700&display=swap">
<style>
  :root{
    --page:#d8d5ea;
    --navy:#2f2c5f;
    --ink:#2b2b33;
    --red:#c1272d;
    --brand:#3d3b78;
    --rule:#9b98b6;
    --photo-a:#cfcbe3;
    --photo-b:#b9b3d3;
  }
  *{box-sizing:border-box;margin:0;padding:0}
  html,body{width:1200px;height:871px;overflow:hidden;background:#fff}
  body{position:relative;font-family:"Carlito","Calibri",Arial,sans-serif;color:var(--ink)}
  .page{position:absolute;top:30px;width:573px;height:810px;background:var(--page);overflow:hidden}
  .page--services{left:22px}
  .page--packages{left:605px}

  .brand{position:absolute;left:44px;display:flex;align-items:center;height:80px}
  .page--services .brand{top:26px}
  .page--packages .brand{top:10px}
  .brand__mark{width:22px;height:22px;border-radius:50%;background:var(--brand);margin-right:10px;flex:none}
  .brand__name{font-family:"Arimo",Arial,sans-serif;font-weight:700;color:var(--brand);font-size:20px;line-height:23px;width:248px;flex:none}
  .brand__divider{width:1px;height:72px;background:var(--rule);margin:0 12px 0 8px;flex:none}
  .brand__tagline{font-family:"Arimo",Arial,sans-serif;color:var(--red);font-size:12.5px;line-height:16px;width:195px;flex:none}

  .photo{position:absolute}
  .photo--team{left:170px;top:420px;width:403px;height:355px;background:radial-gradient(ellipse at 60% 45%,var(--photo-b),var(--photo-a) 60%,var(--page) 85%);opacity:.8}
  .photo--staff{left:0;top:570px;width:573px;height:205px;background:linear-gradient(180deg,var(--page),#a9a3c6 45%,#6d6890)}

  .services{position:absolute;left:28px;top:127px;width:518px}
  .services__title{font-family:"Arimo",Arial,sans-serif;font-weight:700;font-size:19px;line-height:22px;color:var(--navy);margin-bottom:7px}
  .service{font-size:7.6px;line-height:10.5px;text-align:justify;margin-bottom:10px;position:relative}
  .service h3{font-size:7.6px;font-weight:700}

  .packages{position:absolute;left:26px;top:110px;width:528px;font-size:11.4px;line-height:14px}
  .packages__title{font-family:"Arimo",Arial,sans-serif;font-weight:700;font-size:15px;line-height:18px;text-align:center;margin-bottom:15px}
  .package{margin-bottom:14px}
  .package h3{color:var(--red);font-weight:700;font-size:11.4px}
  .package__name{display:inline-block;width:80px}
  .package--salary .package__name{width:69px}
  .package ul{list-style:none;padding-left:21px}
  .package li{position:relative;padding-left:11px}
  .package li::before{content:"•";position:absolute;left:0}
  .note{font-style:italic;padding-left:18px}

  .address{position:absolute;left:0;bottom:0;width:100%;height:35px;color:#fff;font-family:"Arimo",Arial,sans-serif;font-size:19px;line-height:35px;text-align:center}
  .page--services .address{background:var(--navy)}
  .page--packages .address{background:var(--red)}
</style>
</head>
<body>

<section class="page page--services">
  <div class="photo photo--team" role="img" aria-label="Photo of smiling healthcare staff in scrubs and lab coats"></div>
  <header class="brand">
    <span class="brand__mark"></span>
    <span class="brand__name">MERIDIAN HR EMPLOYEE SOLUTIONS</span>
    <span class="brand__divider"></span>
    <span class="brand__tagline">Managing the employee life cycle from recruitment to retirement</span>
  </header>
  <div class="services">
    <h2 class="services__title">MAJOR SERVICE OFFERINGS</h2>
    <div class="service"><h3>Employee Relations</h3><p>We are your HR department. Our staff will work with your management team to ensure quick resolutions to employee issues. Employees will have contact information for the HR team so that they can reach out anytime they need assistance.</p></div>
    <div class="service"><h3>Human Resource Technology (HRIS)</h3><p>PULSE presented by OrbitHRO is the preferred technology vendor of our organization. This powerful system allows small business to access the technology solutions of much larger organizations and includes employee and manager self-service options. PULSE group volume discounts are passed through to all clients of Keystone HR Services.</p></div>
    <div class="service"><h3>Benefit Analysis, Plan Design &amp; Administration</h3><p>Our specialist will work to bring you and your employees a comprehensive benefits package that will include options for health, dental and vision insurance. We will also introduce supplemental products the will offer your employees lower group rates, guaranteed issue, and a variety of coverage. This service includes the administration of your plans throughout the benefits year as well as vendor management and employee assistance.</p></div>
    <div class="service"><h3>Compensation/Incentive Plan Design</h3><p>Once a year we will provide the latest information on our local labor market. This information will assist Keystone HR Services in recommending pay changes based upon the market information for specific positions.</p></div>
    <div class="service"><h3>Employee Job Description Creation</h3><p>Clear communication regarding job duties is a key component in avoiding unnecessary misunderstandings. Job descriptions also serve as a means to clarify performance requirements, recruit for vacancies, train employees, and check for compliance with legal requirements related to equal opportunity, equal pay, overtime eligibility, etc. Creation of job description with an annual update will be provided under this service.</p></div>
    <div class="service"><h3>Employee Handbook</h3><p>Providing employees' with a handbook creates a direct communication resource for the employer and the employee. It provides guidance and information related to the company's history, mission, values, policies, procedures and benefits. It is also viewed as a means of protecting the company against discrimination or unfair treatment claims.</p></div>
    <div class="service"><h3>New Hire On-Boarding</h3><p>Improve productivity, build loyalty, and increase employee success by creating a positive first impression through an effective and efficient on-boarding process.</p></div>
    <div class="service"><h3>Workers Compensation Analysis, Plan Design &amp; Claims Management</h3><p>Working with you we will locate the lowest possible rates for your workers compensation insurance needs. We will manage the process with your vendor when injuries occur on the job.</p></div>
    <div class="service"><h3>Unemployment Claims Administration</h3><p>Many organizations do not realize that their unemployment rate is one area where cost savings can be realized. Through a combination of policy development, employee disciplinary procedures, and a cooperative partnership with the state Unemployment agency we can help to maintain or reduce your unemployment costs.</p></div>
    <div class="service"><h3>Regulatory Compliance</h3><p>Building off of the HR Audit and Risk Assessment our team will work with you to ensure that you are compliant in federal and state regulatory compliance.</p></div>
    <div class="service"><h3>Payroll Administration &amp; Management</h3><p>The service removes the worry of payroll and payroll taxes. Direct Deposit makes paying employees both quick and convenient.</p></div>
    <div class="service"><h3>OSHA Program Development, Training &amp; Compliance</h3><p>The Occupational Safety &amp; Health Administration regulates and enforces federally enacted safety standards for all different types of industries. The healthcare industry has some very specific requirements. We can work with you and your employees to ensure a safe and compliant working environment. This service will include the initial hazard assessment, preparation of your OSHA manual and monthly trainings.</p></div>
    <div class="service"><h3>Recruitment &amp; Pre-Employment Services</h3><p>Hiring the wrong person costs organizations valuable time and money. By developing and consistently following sound recruitment and pre-employment practices companies find that they are better able to manage their turnover. Our recruitment and pre-employment services include sourcing and prescreening candidates. In partnership with our background investigation organization we will thoroughly screen and advise clients in the hiring process.</p></div>
  </div>
  <footer class="address">4310 Ridgeview Parkway, Suite 210 Dallas, Texas 75230</footer>
</section>

<section class="page page--packages">
  <div class="photo photo--staff" role="img" aria-label="Photo of a row of smiling business professionals in suits"></div>
  <header class="brand">
    <span class="brand__mark"></span>
    <span class="brand__name">MERIDIAN HR EMPLOYEE SOLUTIONS</span>
    <span class="brand__divider"></span>
    <span class="brand__tagline">Managing the employee life cycle from recruitment to retirement</span>
  </header>
  <div class="packages">
    <h2 class="packages__title">Recruiting and Staffing Packages</h2>
    <div class="package">
      <h3><span class="package__name">Package A</span>$275.00</h3>
      <ul><li>Source up to 6 resumes</li><li>Position is advertised on 1 job board</li></ul>
      <p class="note">Note: Job Description is provided by client.&nbsp; We can provide this service to you for an additional fee of $35)</p>
    </div>
    <div class="package">
      <h3><span class="package__name">Package B</span>$ 390.00</h3>
      <ul><li>Source up to 8 resumes</li><li>Position advertised on 2 job boards</li><li>Phone screen prospective candidates utilizing position specific requirements and questions provided by Client</li><li>Client will be presented with a summarization of phone screen along with prospective candidates resume</li></ul>
      <p class="note">Note: Job Description is provided by client.&nbsp; We can provide this service to you for an additional fee of $35)</p>
    </div>
    <div class="package">
      <h3><span class="package__name">Package C</span>$ 625.00</h3>
      <ul><li>Source up to 10 resumes</li><li>Create a customized job description that best fits your organizations needs</li><li>Position advertised on 3 job boards</li><li>Phone screen prospective candidates and conduct up to 3 in-person interviews based on position specific requirements</li><li>Client will be presented with a summarization of the interviews, based on a candidate ranking system, as well as the prospective candidates resume</li></ul>
    </div>
    <div class="package package--salary">
      <h3><span class="package__name">Package D</span>Percentage of Prospective Candidates Annual Salary</h3>
      <p>Recruiter will take the time to learn about your organization so they can identify individuals with qualities that will best match with your team. They will source, conduct in-depth interviews via phone and in-person, as well as perform thorough background and reference checks prior to employment. Package also included:</p>
      <ul><li>Create a customized job description that best fits your organizations needs</li><li>Position advertised on 3 job boards</li><li>Client will be presented with a summarization of the interviews, based on a candidate ranking system, as well as the prospective candidates resume</li></ul>
    </div>
  </div>
  <footer class="address">4310 Ridgeview Parkway, Suite 210 Dallas, Texas 75230</footer>
</section>

</body>
</html>
```